Vela Sack new product

Re-usable baby food pouch. Need artwork for new product.
Primarily green, some clear space (1/3 - 1/2 clear) so you can see through to whats inside.

To be fresh, organic looking and to appeal to kids and families.

Portrait style 18xm long, 11cm wide.

Need a front and back version (both this size)

please see similar products on www.brightmorsels.example and www.tinyoakbag.example

Target Market(s)

Families, kids product

Industry/Entity Type

Baby

Colors
9ccb3b

Requirements
Must have
• Clear space as described.
Under Logo
"reusable food pouch"
BPA Free- dishwasher safe- freezer safe

On back
Logo
Tick boxes
Freezer safe
dishwasher safe
BPA Phthalate & PVC Free
160 mls
DO NOT MICROWAVE

"to warm contents simply place filled pouch in a bowl of hot water" Keep the cap out of reach of children 3 and under.

www.kelbirds.example.au

```html
<!DOCTYPE html>
<html lang="en">
<head>
<meta charset="utf-8">
<title>Vela Sack – Reusable Food Pouch</title>
<link rel="stylesheet" href="https://fonts.googleapis.com/css2?family=Fredoka:wght@600&family=Arimo:wght@400;700&display=swap">
<style>
  :root {
    --green: #9ccb3b;
    --green-dark: #8bbb2c;
    --green-tint: #c3e08a;
    --white: #ffffff;
    --clear: #e4e6e6;
    --bg: #f1f1f1;
    --ink: #4a4a4a;
  }
  * { box-sizing: border-box; margin: 0; padding: 0; }
  html, body { width: 1196px; height: 1200px; overflow: hidden; }
  body {
    background: radial-gradient(ellipse at 50% 40%, #ffffff 0%, var(--bg) 70%, #e6e6e6 100%);
    font-family: "Arimo", Arial, sans-serif;
    position: relative;
  }
  .pouch { position: absolute; }
  .pouch-shape { position: absolute; inset: 0; }
  .pouch-shape path { fill: var(--green); }
  .pouch-front { left: 164px; top: 57px; width: 488px; height: 900px; }
  .pouch-back { left: 680px; top: 57px; width: 440px; height: 800px; }

  .brand {
    position: absolute; left: 0; right: 0;
    display: flex; align-items: center; justify-content: center; gap: 14px;
    font-family: "Fredoka", sans-serif; font-weight: 600; color: var(--white);
    line-height: 1;
  }
  .brand-dot { border-radius: 50%; background: var(--white); flex: none; }
  .tagline {
    position: absolute; left: 50%; transform: translateX(-50%);
    background: var(--white); color: var(--green);
    font-family: "Arimo", sans-serif; font-weight: 700;
    border-radius: 999px; white-space: nowrap; text-align: center;
  }

  .pouch-front .brand { top: 330px; font-size: 64px; }
  .pouch-front .brand-dot { width: 58px; height: 58px; }
  .pouch-front .tagline { top: 432px; font-size: 23px; padding: 6px 20px; border: 3px solid var(--white); }
  .clear-window {
    position: absolute; left: 62px; top: 500px; width: 364px; height: 320px;
    background: var(--clear); border-radius: 150px 150px 160px 160px;
  }
  .claims {
    position: absolute; left: 0; right: 0; top: 820px;
    display: flex; justify-content: center; gap: 48px;
    color: var(--white); text-align: center;
  }
  .claim { display: flex; flex-direction: column; align-items: center; width: 90px; }
  .claim svg { width: 36px; height: 36px; margin-bottom: 4px; }
  .claim-small { font-size: 11px; font-weight: 700; letter-spacing: 0.3px; }
  .claim-big { font-size: 17px; font-weight: 700; letter-spacing: 0.5px; }

  .pouch-back .brand { top: 250px; font-size: 44px; }
  .pouch-back .brand-dot { width: 40px; height: 40px; }
  .pouch-back .tagline { top: 322px; font-size: 15px; padding: 4px 14px; }
  .checklist { position: absolute; left: 58px; top: 372px; list-style: none; color: var(--white); }
  .checklist li {
    display: flex; align-items: center; gap: 12px;
    font-size: 18px; font-weight: 700; height: 36px;
  }
  .checklist svg { width: 24px; height: 24px; flex: none; }
  .fill-note {
    position: absolute; left: 50%; top: 560px; transform: translateX(-50%);
    width: 120px; text-align: center; color: var(--white);
  }
  .fill-note span { display: block; font-size: 8px; letter-spacing: 0.5px; margin-bottom: 3px; }
  .fill-note div { height: 28px; border: 1.5px solid var(--white); border-radius: 5px; background: var(--green-tint); }
  .warm-box {
    position: absolute; left: 60px; right: 50px; top: 620px;
    background: var(--white); color: var(--green); border-radius: 14px;
    padding: 10px 14px; text-align: center; font-weight: 700; font-size: 14px; line-height: 1.35;
  }
  .web { position: absolute; left: 0; right: 0; top: 730px; text-align: center; color: var(--white); font-size: 16px; font-weight: 700; }

  .legend {
    position: absolute; left: 30px; top: 1036px; width: 630px; height: 142px;
    border: 4px solid var(--green); border-radius: 26px;
    display: grid; grid-template-columns: 300px 1fr; row-gap: 18px; align-content: center;
    padding: 0 28px; color: var(--ink); font-size: 19px;
  }
  .swatch-row { display: flex; align-items: center; gap: 14px; }
  .swatch { width: 24px; height: 24px; border: 1px solid #cfcfcf; }
  .swatch-green { background: var(--green); }
  .swatch-tint { background: var(--green-tint); }
  .swatch-white { background: var(--white); }
  .swatch-clear { background: var(--clear); }

  .lockup { position: absolute; left: 748px; top: 1000px; width: 400px; height: 150px; }
  .lockup .brand { top: 8px; font-size: 66px; color: var(--green); }
  .lockup .brand-dot { width: 60px; height: 60px; background: var(--green); }
  .lockup .tagline {
    top: 102px; background: var(--green); color: var(--white);
    font-size: 26px; padding: 5px 18px;
  }
</style>
</head>
<body>

<section class="pouch pouch-front" aria-label="Front of pouch">
  <svg class="pouch-shape" viewBox="0 0 488 900" aria-hidden="true">
    <path d="M92,12 Q92,0 104,0 H384 Q396,0 396,12 V70 Q396,112 446,124 L470,130 Q488,134 488,152 V880 Q488,900 468,900 H20 Q0,900 0,880 V250 Q0,232 14,222 L70,180 Q92,162 92,130 Z"/>
  </svg>
  <div class="brand"><span class="brand-dot"></span>Vela Sack</div>
  <div class="tagline">REUSABLE FOOD POUCH</div>
  <div class="clear-window" role="img" aria-label="Clear window showing the pouch contents"></div>
  <div class="claims">
    <div class="claim">
      <svg viewBox="0 0 36 36" fill="none" stroke="#fff" stroke-width="2.5"><rect x="6" y="4" width="24" height="28" rx="4"/><circle cx="18" cy="20" r="7"/><line x1="10" y1="9" x2="26" y2="9"/></svg>
      <span class="claim-small">DISHWASHER</span><span class="claim-big">SAFE</span>
    </div>
    <div class="claim">
      <svg viewBox="0 0 36 36"><path d="M8,30 C8,14 18,6 30,6 C30,20 22,30 8,30 Z" fill="#fff"/></svg>
      <span class="claim-small">BPA</span><span class="claim-big">FREE</span>
    </div>
    <div class="claim">
      <svg viewBox="0 0 36 36" stroke="#fff" stroke-width="3" stroke-linecap="round"><line x1="18" y1="3" x2="18" y2="33"/><line x1="5" y1="10.5" x2="31" y2="25.5"/><line x1="5" y1="25.5" x2="31" y2="10.5"/></svg>
      <span class="claim-small">FREEZER</span><span class="claim-big">SAFE</span>
    </div>
  </div>
</section>

<section class="pouch pouch-back" aria-label="Back of pouch">
  <svg class="pouch-shape" viewBox="0 0 440 800" aria-hidden="true">
    <path d="M60,12 Q60,0 72,0 H336 Q348,0 348,12 V120 Q348,150 380,176 L420,206 Q440,220 440,240 V780 Q440,800 420,800 H20 Q0,800 0,780 V140 Q0,122 18,118 L38,112 Q60,104 60,70 Z"/>
  </svg>
  <div class="brand"><span class="brand-dot"></span>Vela Sack</div>
  <div class="tagline">REUSABLE FOOD POUCH</div>
  <ul class="checklist">
    <li><svg viewBox="0 0 24 24" fill="none" stroke="#fff" stroke-width="2"><rect x="2" y="4" width="18" height="18"/><path d="M6,12 L11,18 L22,2"/></svg>Freezer safe</li>
    <li><svg viewBox="0 0 24 24" fill="none" stroke="#fff" stroke-width="2"><rect x="2" y="4" width="18" height="18"/><path d="M6,12 L11,18 L22,2"/></svg>dishwasher safe</li>
    <li><svg viewBox="0 0 24 24" fill="none" stroke="#fff" stroke-width="2"><rect x="2" y="4" width="18" height="18"/><path d="M6,12 L11,18 L22,2"/></svg>BPA Phthalate &amp; PVC Free</li>
    <li><svg viewBox="0 0 24 24" fill="none" stroke="#fff" stroke-width="2"><rect x="2" y="4" width="18" height="18"/><path d="M6,12 L11,18 L22,2"/></svg>160 mls</li>
    <li><svg viewBox="0 0 24 24" fill="none" stroke="#fff" stroke-width="2"><rect x="2" y="4" width="18" height="18"/><path d="M5,7 L19,21 M19,7 L5,21"/></svg>DO NOT MICROWAVE</li>
  </ul>
  <div class="fill-note"><span>EASY FILL WITH</span><div role="img" aria-label="Filling accessories"></div></div>
  <div class="warm-box">To warm contents simply place filled pouch in a bowl of hot water.<br>Keep the cap out of reach of children 3 and under.</div>
  <div class="web">www.kelbirds.example.au</div>
</section>

<section class="legend" aria-label="Colour key">
  <div class="swatch-row"><span class="swatch swatch-green"></span>Green Vela Sack (C44 Y100)</div>
  <div class="swatch-row"><span class="swatch swatch-tint"></span>65% Tint of Green Vela Sack</div>
  <div class="swatch-row"><span class="swatch swatch-white"></span>White</div>
  <div class="swatch-row"><span class="swatch swatch-clear"></span>Clear space</div>
</section>

<section class="lockup" aria-label="Brand lockup">
  <div class="brand"><span class="brand-dot"></span>Vela Sack</div>
  <div class="tagline">REUSABLE FOOD POUCH</div>
</section>

</body>
</html>
```